Harvest Wing Guild Needs an Infographic

We are looking for an engaging infographic that will illustrate the steps and skill set needed to become an agricultural pilot. The infographic will be used in print and on the web. Print formats could include an 8.5" x 11" page or 17" x 11" spread/poster in a magazine and should also be scalable so that it can be printed as a larger poster. The web-ready infographic will be used on the association's website and Chirpbook page. Agricultural aviation is an exciting profession, but it is not always apparent or easy to get started in the industry. This infographic will focus on the requirements, training options, skills/mindset, working conditions, and income potential for someone interested in becoming an agricultural pilot, as well as the need for agricultural aviation services. The working title for the infographic is, "The Hunt for the Nation's Fresh Field Flyers Begins!" I am uploading a Word document with the proposed text. What we would like a graphic designer to do is turn that text into something highly visual/graphical. The supplied text can be pared down, if necessary, or used as a guide to accomplish the appropriate balance between the words, images, and graphics. The final design should be professional but appeal to people, primarily males, between the ages of 17-30.
Updates

We have increased the budget for our infographic design project!

Project Deadline Extended
Reason: We have extended our deadline to give designers interested in submitting an infographic design more time. We would appreciate any designs you can send our way!

Target Market(s)

This infographic is aimed at people between the ages of 17-30, predominantly males, interested flying and a possible career in agricultural aviation. A lot of people may be pilots who are interested in agricultural aviation, but they don't know how go about it. Typically, potential ag pilots have lived in a rural area and enjoy the outdoors. Due to the small size of the industry, agricultural aviation can be challenging to get into. We want this infographic to shed some light on that process in a way that will resonate with a younger generation. If you need more information, please visit www.fieldsoarers.example/content/start-here.

Industry/Entity Type

Graphic Designer

Font styles to use
Serif
Sans Serif

Requirements
Must have
• 1) The infographic should follow the general format provided in the Ag-Pilot-Career-Infographic-Concept document. It does not have to literally follow that format (for instance, I used bullet points), but it should convey and, depending on how much creative license you use, at least capture the essence of the factors outlined in the document for becoming an ag pilot. It would be preferable for the infographic to be in portrait format in case it is made into a poster. The infographic should end with our logo and web address.
2) The infographic should also feature illustrations of ag planes (a.k.a. crop dusters), but they have to be of actual agricultural aircraft. An open-cockpit biplane is not an ag plane.
3) All images must be royalty-free and obtained legally. If you choose to use stock art, start with the comp image until the artwork is approved.
Nice to have
• 1) Agricultural images/illustrations, such as corn, wheat or cotton.
2) Icons of a growing crowd of people to illustrate 8.1 billion people by 2025 and a population of 9.6 billion people by 2050.
Should not have
• Crop dusting is an outdated term. Aerial applicators do not apply dust, products are primarily dispensed in liquid form. Therefore, do not use any imagery featuring plumes of smoke coming from the airplane or helicopter. Also, although the current pool of ag pilots is getting older, the infographic should not make them appear geriatric or elderly.

```html
<!DOCTYPE html>
<html lang="en">
<head>
<meta charset="utf-8">
<title>The Hunt for the Nation's Fresh Field Flyers Begins!</title>
<link rel="stylesheet" href="https://fonts.googleapis.com/css2?family=PT+Sans+Narrow:wght@700&family=Arimo:ital,wght@0,400;0,700;1,400;1,700&display=swap">
<style>
:root{
  --navy:#0e3f8c;
  --card-head:#1a58a6;
  --green:#2f9a3f;
  --accent:#2b9b3a;
  --ink:#1b1b1b;
  --muted:#3c3c3c;
  --sky-top:#cfe6f5;
  --sky-bottom:#eef6fb;
  --white:#ffffff;
}
*{box-sizing:border-box;margin:0;padding:0}
html,body{width:1200px;height:776px;overflow:hidden;background:var(--white)}
body{font-family:"Arimo",Arial,sans-serif;color:var(--ink);position:relative}
.hero-photo{position:absolute;left:0;top:0;width:415px;height:270px;
  background:linear-gradient(180deg,#4a6a3e 0%,#5d7f47 45%,#88a85a 62%,#6f9b3f 100%)}
.title-band{position:absolute;left:415px;top:0;width:785px;height:78px;background:var(--navy);
  display:flex;align-items:center;padding-left:16px}
.title-band h1{font-family:"PT Sans Narrow",sans-serif;color:var(--white);font-size:36px;letter-spacing:-.2px;white-space:nowrap}
.intro{position:absolute;left:430px;top:93px;width:386px;font-size:12.4px;line-height:20px;color:var(--muted)}
.intro strong{color:var(--card-head)}
.stats{position:absolute;left:830px;top:78px;width:356px;height:158px;background:var(--green);
  border-radius:0 0 8px 8px;padding:12px 14px 0 18px;color:var(--white);list-style:none}
.stats li{display:flex;gap:10px;margin-bottom:9px;font-size:13px;font-style:italic;line-height:15px}
.stats .star{font-style:normal;font-size:16px}
.stats b{font-style:normal;font-size:17px;margin-right:4px}
.tagline{position:absolute;left:430px;top:243px;font-family:"PT Sans Narrow",sans-serif;font-size:24px;color:var(--navy);white-space:nowrap}
.details{position:absolute;left:0;top:270px;width:1200px;height:402px;
  background:linear-gradient(180deg,var(--sky-top),var(--sky-bottom))}
.card{position:absolute;top:17px;width:226px;height:376px;background:var(--white);border-radius:8px;overflow:hidden;
  box-shadow:0 1px 4px rgba(0,0,0,.25)}
.card-photo{height:83px}
.card h2{height:25px;background:var(--card-head);color:var(--white);font-size:14px;font-weight:700;text-align:center;line-height:25px}
.card ul{list-style:none;padding:8px 10px 0 10px}
.card li{position:relative;padding-left:16px;margin-bottom:8px}
.card li::before{content:"";position:absolute;left:0;top:2px;width:8px;height:8px;border:1.5px solid var(--accent);border-radius:50%;
  background:radial-gradient(circle,var(--accent) 35%,transparent 40%)}
.card .lead{font-size:10.6px;font-weight:700;line-height:12.5px;display:block}
.card p{font-size:8.2px;font-style:italic;line-height:10px;color:var(--muted);margin-top:2px}
.card em.hl{color:var(--accent);font-weight:700}
.photo-cockpit{background:linear-gradient(180deg,#9fb7c4,#3f4a4f 55%,#23292b)}
.photo-pilots{background:linear-gradient(135deg,#5f6d45,#a8b6bd 50%,#e0c64a)}
.photo-heli{background:linear-gradient(180deg,#c9dbe8 0%,#a9c6dd 45%,#6a9a45 60%,#4f7d33)}
.photo-hangar{background:linear-gradient(180deg,#6c7a55,#c7c98a 50%,#6b6a3a)}
.photo-plane{background:linear-gradient(180deg,#8aa0b3,#5c6c5b 60%,#3c4a3a)}
.footer-brand{position:absolute;left:55px;top:700px;display:flex;align-items:center;gap:12px}
.footer-brand .dot{width:38px;height:38px;border-radius:50%;background:var(--card-head)}
.footer-brand span{font-size:26px;font-weight:700;color:var(--card-head);letter-spacing:1px}
.need{position:absolute;left:483px;top:679px;width:705px}
.need h3{font-size:15px;color:var(--card-head);margin-bottom:5px}
.need ul{list-style:none}
.need li{font-size:10.2px;line-height:15px;color:var(--muted);padding-left:16px;position:relative}
.need li::before{content:"";position:absolute;left:3px;top:5px;width:5px;height:5px;border-radius:50%;background:var(--accent)}
.need .more{font-size:9.5px;font-style:italic;color:var(--muted);margin-top:7px}
.need .more b{font-style:normal;color:var(--accent);font-size:12px}
</style>
</head>
<body>
<div class="hero-photo" role="img" aria-label="Photo of a white and red agricultural aircraft flying low over a green field in front of trees"></div>
<header class="title-band"><h1>The Hunt for the Nation's Fresh Field Flyers Begins!</h1></header>
<p class="intro"><strong>Aerial application</strong> is an exciting field that combines precision agriculture with low-level aviation to aid farmers in producing a safe, affordable and abundant supply of food, fiber and biofuel. To those who are a part of this unique profession, it's not just a job but a way of life. Becoming an ag pilot isn't easy, but it is worth it. As agriculture's air force ages, the window of opportunity is open for a new generation of ag pilots to step forward and provide the aerial application services America's farmers depend on.</p>
<ul class="stats">
  <li><span class="star">★</span><span><b>2,700</b>Number of ag pilots in the United States</span></li>
  <li><span class="star">★</span><span><b>50+</b>Average age of ag pilots in the U.S.</span></li>
  <li><span class="star">★</span><span><b>71 million</b>Acres aerial applicators treat by air each year in the U.S.</span></li>
  <li><span class="star">★</span><span><b>8.1 billion</b>Projected world population in 2025, up from 7.2 billion in 2013</span></li>
</ul>
<p class="tagline">Think you've got the right stuff? Here's what it takes to enter and make it as an ag pilot.</p>

<section class="details">
  <article class="card" style="left:12px">
    <div class="card-photo photo-cockpit" role="img" aria-label="Photo of an ag aircraft cockpit instrument panel"></div>
    <h2>Requirements</h2>
    <ul>
      <li><span class="lead">Commercial Pilot Certificate</span></li>
      <li><span class="lead">Class II Medical Certificate (annual examination)</span></li>
      <li><span class="lead">Trained and tested in agricultural aircraft operations</span><p>Ag pilots must <em class="hl">pass a knowledge &amp; skills test</em> administered by the Air Safety Board or the pilot's chief operations supervisor.</p></li>
      <li><span class="lead">State-administered CPA commercial pesticide applicator certification</span><p>Ag pilots must <em class="hl">obtain a pesticide license</em> in each state they fly in demonstrating their knowledge in the handling and application of crop protection products.</p></li>
      <li><span class="lead">Meet the requirements for insurability in the aircraft and type of flight operations</span></li>
    </ul>
  </article>
  <article class="card" style="left:250px">
    <div class="card-photo photo-pilots" role="img" aria-label="Photo of an instructor and a student pilot beside a yellow ag plane"></div>
    <h2>Training Options</h2>
    <ul>
      <li><span class="lead">Preparatory Education</span><p><em class="hl">Basic flight training program</em> at a flight school, or flight training curriculum at a two-or four-year college</p><p><em class="hl">Agricultural coursework</em> at a university, college, community college or other institution. (A college degree is not mandatory, but many incoming ag pilots have a degree in agro-science or business. Others have a more aviation-focused education.)</p></li>
      <li><span class="lead">Attend a flight school specializing in agricultural aviation training</span></li>
      <li><span class="lead">On-the-Job Training/Apprenticeship</span><p>Being trained under an experienced aerial application operator is an excellent way to get the on-the-job training needed to become a safe, efficient ag pilot. This could include <em class="hl">learning from the ground up</em> as a mixer/loader for a period of time.</p></li>
    </ul>
  </article>
  <article class="card" style="left:487px">
    <div class="card-photo photo-heli" role="img" aria-label="Photo of a white and blue ag helicopter hovering over a crop field"></div>
    <h2>Skills/Mindset</h2>
    <ul>
      <li><span class="lead">Flying is a big part of the job, but just one of many facets of being an ag pilot.</span><p>Ag pilots are often referred to as <em class="hl">"farmers in the sky"</em> because of the amount of agricultural knowledge required to ensure the job is completed correctly and safely without incurring economical or environmental damage to persons or property.</p><p>While being an aircraft mechanic is not a requirement, <em class="hl">mechanical knowledge</em> is helpful.</p><p><em class="hl">Good communication skills</em> to deal with customers and the community are important.</p><p>Finally, an aspiring ag pilot must have a <em class="hl">deep desire</em> to pursue this career path. That fortitude will serve you well.</p></li>
    </ul>
  </article>
  <article class="card" style="left:723px">
    <div class="card-photo photo-hangar" role="img" aria-label="Photo of ag aircraft parked inside a hangar"></div>
    <h2>Working Conditions</h2>
    <ul>
      <li><span class="lead">If you are a "rookie," expect one to two years of learning the ground operation with a gradual transition to flight operations.</span></li>
      <li><span class="lead">During the flying season, expect LONG days.</span><p>In the summer ag pilots are <em class="hl">airborne by sunrise</em>. They work until the work runs out, the temperature is too hot to effectively apply product or the sun goes down. In certain areas applications are conducted during nighttime hours as well.</p><p>During the busy season some operators/pilots work <em class="hl">seven days a week</em> while the work is available.</p></li>
      <li><span class="lead">During the offseason...</span><p>Ag pilots <em class="hl">complete any required recurring training</em> and earn continuing education credits at state and national agricultural aviation conventions.</p><p><em class="hl">The seasonal nature of ag flying</em> in many areas may afford ag pilots with the opportunity for time off or to supplement their income through other forms of work.</p></li>
    </ul>
  </article>
  <article class="card" style="left:960px">
    <div class="card-photo photo-plane" role="img" aria-label="Photo of a white and red ag plane on the ramp at dusk"></div>
    <h2>Income Potential</h2>
    <ul>
      <li><span class="lead">Most ag pilots are paid based on the amount of acres they treat.</span></li>
      <li><span class="lead">Initially, the pay will be lower while you work on the ground learning the ropes.</span></li>
      <li><span class="lead">Once you start to fly and perform aerial applications the pay improves.</span></li>
      <li><span class="lead">Once in the air many first-year ag pilots can average $20,000–$40,000 depending on the quantity and type of aerial application work performed.</span></li>
      <li><span class="lead">Skilled aerial applicators can make $60,000–$100,000 a year, the <i>Daily Ledger Review</i> reports.</span></li>
    </ul>
  </article>
</section>

<div class="footer-brand"><div class="dot"></div><span>HARVEST WING GUILD</span></div>
<section class="need">
  <h3>Need for Aerial Application</h3>
  <ul>
    <li>Aerial application is often the safest, fastest, most efficient and most economical way to treat a crop when pests or disease threaten it.</li>
    <li>By 2050 there will be 9.6 billion people on the planet. That's 2.4 billion more mouths to feed compared to today. That's why...</li>
    <li>There will always be a need for professional, well-trained ag pilots!</li>
  </ul>
  <p class="more">For more information on careers in the ag aviation industry or to join the Guild for access to a network of aerial applicators nationwide, visit <b>www.fieldsoarers.example</b></p>
</section>
</body>
</html>
```